Business Card Design

I need a business card for my company i am starting. I will be providing stump grinding services. I use a motorized machine to grind stumps down under the ground so that they are out of the way and out of sight. I'm looking for my card to have maroon or dark red somewhere in the card to match my truck. I'm going to use this card to advertise and also serve as a design to wrap my truck tailgate as advertisement so i want it to match. the dark maroon color of my truck. I wouldn't mind using bright colors or color for the rest of the card or the lettering or any designs on the card. In the images i have provided i like how there are saw blades integrated into these people advertisements. I also like the illustration of the stump grinder. I also provided a picture of the actual cutting wheel or blade of the grinder.

Industry/Entity Type

Business

Contact Information for Business Card

Company Name - Oakline Stump Grinding
Phone - 407-219-5573
Email - harlow.stumpwork@quillpost.net
Name and title - Thomas Harlow - Owner and operator
Company Slogan - You find them, I'll grind them

```html
<!DOCTYPE html>
<html lang="en">
<head>
<meta charset="utf-8">
<title>Oakline Stump Grinding – Business Card</title>
<link rel="stylesheet" href="https://fonts.googleapis.com/css2?family=Raleway:wght@400;500;600;700&display=swap">
<style>
  :root {
    --maroon: #431112;
    --grinder-red: #7d1517;
    --paper: #ffffff;
    --ink-light: #ffffff;
  }
  html, body {
    margin: 0;
    padding: 0;
    overflow: hidden;
    background: var(--paper);
  }
  .card {
    position: relative;
    width: 1200px;
    height: 703px;
    overflow: hidden;
    background: var(--paper);
    font-family: "Raleway", sans-serif;
    color: var(--ink-light);
  }
  .card__panel {
    position: absolute;
    inset: 0;
    width: 1200px;
    height: 703px;
  }
  .card__wheel {
    position: absolute;
    left: 740px;
    top: -30px;
    width: 550px;
    height: 550px;
  }
  .brand {
    position: absolute;
    left: 57px;
    top: 46px;
    white-space: nowrap;
  }
  .brand__name {
    margin: 0;
    font-size: 44px;
    font-weight: 600;
    line-height: 1;
    letter-spacing: 0;
  }
  .brand__slogan {
    margin: 12px 0 0;
    font-size: 24px;
    font-weight: 400;
    line-height: 1;
  }
  .person {
    position: absolute;
    left: 57px;
    top: 280px;
    white-space: nowrap;
  }
  .person__name {
    margin: 0;
    font-size: 75px;
    font-weight: 600;
    line-height: 1;
    letter-spacing: 0.5px;
  }
  .person__rule {
    width: 388px;
    height: 3px;
    margin: 14px 0 0;
    border: 0;
    background: var(--ink-light);
  }
  .person__title {
    margin: 14px 0 0;
    font-size: 44px;
    font-weight: 400;
    line-height: 1;
  }
  .contact {
    position: absolute;
    left: 57px;
    top: 556px;
    margin: 0;
    padding: 0;
    list-style: none;
    white-space: nowrap;
  }
  .contact__item {
    display: flex;
    align-items: center;
    height: 48px;
    font-size: 29px;
    font-weight: 400;
  }
  .contact__icon {
    width: 42px;
    height: 32px;
    margin-right: 23px;
    fill: var(--ink-light);
  }
</style>
</head>
<body>
<div class="card">
  <svg class="card__panel" viewBox="0 0 1200 703" aria-hidden="true">
    <polygon points="0,0 553,0 957,703 0,703" fill="var(--maroon)"/>
  </svg>

  <svg class="card__wheel" viewBox="0 0 550 550" role="img" aria-label="Illustration of a red stump grinder cutting wheel with teeth and wood chips">
    <defs>
      <radialGradient id="wheelTone" cx="50%" cy="50%" r="50%">
        <stop offset="0%" stop-color="var(--maroon)"/>
        <stop offset="100%" stop-color="var(--grinder-red)"/>
      </radialGradient>
    </defs>
    <circle cx="272" cy="266" r="255" fill="url(#wheelTone)"/>
  </svg>

  <header class="brand">
    <h1 class="brand__name">Oakline Stump Grinding</h1>
    <p class="brand__slogan">You find them, I'll grind them!</p>
  </header>

  <section class="person">
    <h2 class="person__name">Thomas Harlow</h2>
    <hr class="person__rule">
    <p class="person__title">Owner &amp; Operator</p>
  </section>

  <ul class="contact">
    <li class="contact__item">
      <svg class="contact__icon" viewBox="0 0 42 32" aria-hidden="true">
        <path d="M2 10 C2 2 40 2 40 10 L40 13 L31 13 L30 8 L12 8 L11 13 L2 13 Z"/>
        <path d="M10 14 L32 14 L38 28 Q38 31 35 31 L7 31 Q4 31 4 28 Z"/>
        <circle cx="21" cy="22" r="5" fill="var(--maroon)"/>
        <circle cx="21" cy="22" r="2"/>
      </svg>
      407-219-5573
    </li>
    <li class="contact__item">
      <svg class="contact__icon" viewBox="0 0 42 32" aria-hidden="true">
        <path d="M2 5 H40 V27 H2 Z M5 8 V24 H37 V8 L21 19 Z M7 7 L21 17 L35 7 Z" fill-rule="evenodd"/>
      </svg>
      harlow.stumpwork@quillpost.net
    </li>
  </ul>
</div>
</body>
</html>
```